website update

We need to redesign our current website to be more personalised and sophisticated. We are physiotherapy clinic based in sydney australia, offer a range of clinical service such as Physiotherapy, Massage, sports injuries rehabilitation, Women's health (incontinency etc), Pilates classes, back pain exercise program, acupuncture, Gait analysis.
our current website is www.tidewellrehab.com.au
an example of ideal website is http://orchardlanekinetics.com/
homepage: with a revolving displaying attached photos which is linked to relevants page

```html
<!DOCTYPE html>
<html lang="en">
<head>
<meta charset="utf-8">
<title>Tidewell Rehab – Physiotherapy &amp; Sports Clinic</title>
<link rel="stylesheet" href="https://fonts.googleapis.com/css2?family=Oswald:wght@300;400;500&family=Open+Sans:wght@400;600;700&display=swap">
<style>
:root{
  --lime:#8cc63e;
  --lime-light:#a9d15c;
  --green:#2f9f5a;
  --green-dark:#25874b;
  --ink:#3d3d3d;
  --muted:#8a8a8a;
  --bar:#4a4a4a;
  --bar-dark:#5a5a5a;
  --footer:#ececec;
  --white:#ffffff;
  --head:'Oswald',sans-serif;
  --body:'Open Sans',sans-serif;
}
*{box-sizing:border-box;margin:0;padding:0}
html,body{width:1200px;height:2727px;overflow:hidden;background:var(--white);font-family:var(--body);color:var(--ink)}
.wrap{width:1030px;margin:0 auto;position:relative}
ul{list-style:none}

/* top bar */
.topbar{height:31px;background:#f4f4f4}
.topbar .wrap{height:31px;display:flex;justify-content:flex-end;align-items:center}
.social-mini{display:flex;gap:12px;margin-right:22px}
.social-mini span{width:14px;height:14px;border-radius:50%;background:#8a8a8a}
.appt-btn{height:31px;width:231px;background:var(--bar-dark);color:#fff;font-size:11px;display:flex;align-items:center;gap:10px;padding-left:14px;text-transform:uppercase}
.appt-btn svg{flex:none}

/* header */
.header{height:105px}
.header .wrap{height:105px;display:flex;justify-content:space-between;align-items:center}
.brand{display:flex;align-items:center;gap:12px}
.brand-mark{width:58px;height:58px;border-radius:50%;background:var(--lime)}
.brand-name{font-family:var(--head);font-weight:500;font-size:36px;line-height:1;color:var(--lime)}
.brand-sub{font-size:10px;color:var(--muted);letter-spacing:.3px;margin-top:3px}
.contact{text-align:left;margin-top:-12px}
.contact .phone{font-family:var(--head);color:var(--green);font-size:16px;display:flex;align-items:center;gap:6px}
.contact .addr{font-size:10.5px;color:var(--muted);margin-top:6px}

/* nav */
.nav{height:48px;background:var(--green);border-top:4px solid var(--lime)}
.nav ul{display:flex;height:44px;align-items:stretch}
.nav li{font-size:12px;color:#fff;text-transform:uppercase;display:flex;align-items:center;padding:0 25px;letter-spacing:.2px}
.nav li.active{background:var(--lime)}

/* hero */
.hero{height:663px;position:relative;background:linear-gradient(100deg,#d9d9d9 0%,#bdbdbd 40%,#a8a8a8 60%,#d6d6d6 100%)}
.hero-photo{position:absolute;inset:0}
.hero-card{position:absolute;left:698px;top:189px;width:502px;height:311px;background:linear-gradient(160deg,var(--lime) 0%,var(--green) 100%);padding:44px 0 0 45px;color:#fff}
.hero-card h1{font-family:var(--head);font-weight:500;font-size:45px;line-height:1.1;text-transform:uppercase}
.hero-card p{font-family:var(--head);font-weight:400;font-size:27px;line-height:1.3;margin-top:20px}
.dots{display:flex;gap:9px;position:absolute;left:45px;bottom:36px}
.dots span{width:12px;height:12px;border:1.5px solid #fff}
.dots span.on{background:#fff}

/* intro */
.intro{padding-top:76px;height:431px}
.intro .wrap{display:flex;justify-content:space-between}
.section-title{font-family:var(--head);font-weight:300;font-size:25px;color:var(--ink);margin-bottom:25px}
.welcome{width:635px}
.welcome-body{display:flex;gap:20px}
.welcome-photo{width:200px;height:207px;flex:none;background:linear-gradient(135deg,#e4e6e8,#9aa4ab 60%,#3b4248)}
.welcome-lead{font-size:13px;color:var(--lime);text-transform:uppercase;line-height:1.5;margin-bottom:12px}
.welcome-text{font-size:11.5px;color:var(--muted);line-height:1.8}
.news{width:311px}
.news-item{display:flex;gap:20px;padding-bottom:18px;margin-bottom:18px;border-bottom:1px solid #e6e6e6}
.news-item:last-child{border:0}
.news-date{width:55px;height:84px;background:var(--lime);color:#fff;text-align:center;flex:none;position:relative}
.news-date b{display:block;font-family:var(--head);font-weight:300;font-size:30px;padding-top:8px}
.news-date small{font-size:10px;text-transform:uppercase}
.news-date::after{content:"";position:absolute;right:-9px;top:14px;border:9px solid transparent;border-right:0;border-left-color:var(--lime)}
.news-title{font-size:12.5px;color:var(--green);text-transform:uppercase;font-weight:600}
.news-kicker{font-size:9.5px;color:var(--lime);text-transform:uppercase;margin:2px 0 6px}
.news-text{font-size:10.5px;color:var(--muted);line-height:1.6}

/* services */
.services{display:grid;grid-template-columns:repeat(4,257.5px);grid-auto-rows:248px}
.tile-photo{position:relative}
.tile{position:relative;color:#fff;padding:20px 30px}
.tile.lime{background:var(--lime)}
.tile.light{background:var(--lime-light)}
.tile.deep{background:var(--green)}
.tile::before{content:"";position:absolute;top:50%;margin-top:-14px;border:14px solid transparent}
.tile.point-left::before{left:-14px;border-left:0;border-right-color:inherit}
.tile.point-right::before{right:-14px;border-right:0;border-left-color:inherit}
.tile.lime{border-color:var(--lime)}
.tile.light{border-color:var(--lime-light)}
.tile.deep{border-color:var(--green)}
.tile-icon{width:72px;height:72px;border-radius:50%;background:rgba(255,255,255,.25);margin:-2px 0 8px -10px}
.tile h3{font-family:var(--head);font-weight:400;font-size:27px;line-height:1.15;margin-bottom:14px}
.tile p{font-size:12.5px;line-height:1.35}
.tile .more{font-size:10.5px;text-transform:uppercase;margin-top:14px;display:block}
.tile.low{padding-top:68px}
.z1{z-index:1}

/* footer lists */
.lists{background:var(--bar);height:349px;margin-top:67px;padding-top:38px}
.lists .wrap{display:grid;grid-template-columns:384px 367px 279px}
.lists h4{font-family:var(--head);font-weight:300;font-size:25px;color:#fff;margin-bottom:16px}
.lists li{font-size:12.5px;color:#d9d9d9;line-height:25.5px;padding-left:14px;position:relative}
.lists li::before{content:"›";position:absolute;left:0;color:#bbb}
.lists .details{font-size:12.5px;color:var(--lime);margin:12px 0 0 14px;display:block}

/* partners */
.partners{height:131px;display:flex;justify-content:center;align-items:center;gap:42px}
.partner{height:28px;background:#3f3f3f;border-radius:3px}

/* bottom */
.bottom{background:var(--footer);height:156px}
.bottom .wrap{height:156px;display:flex;align-items:center}
.bottom .brand-mark{background:#8a8a8a;width:60px;height:60px}
.bottom .brand-name{color:#6a6a6a}
.bottom .brand{width:344px;margin-left:12px}
.info{width:227px;font-size:12.5px;line-height:1.6;color:#555}
.info h5{font-size:13px;color:var(--green);font-weight:600;margin-bottom:2px}
.social{display:flex;gap:22px;margin-left:24px}
.social span{width:38px;height:38px;border-radius:50%;border:2px solid #a8a8a8}
</style>
</head>
<body>

<div class="topbar">
  <div class="wrap">
    <div class="social-mini"><span></span><span></span><span></span><span></span></div>
    <div class="appt-btn">
      <svg width="16" height="16" viewBox="0 0 16 16"><rect x="1" y="3" width="14" height="12" rx="1" fill="none" stroke="#fff" stroke-width="1.5"/><line x1="1" y1="7" x2="15" y2="7" stroke="#fff" stroke-width="1.5"/><line x1="5" y1="1" x2="5" y2="4" stroke="#fff" stroke-width="1.5"/><line x1="11" y1="1" x2="11" y2="4" stroke="#fff" stroke-width="1.5"/></svg>
      Schedule an appointment online
    </div>
  </div>
</div>

<header class="header">
  <div class="wrap">
    <div class="brand">
      <span class="brand-mark"></span>
      <div>
        <div class="brand-name">tidewellrehab</div>
        <div class="brand-sub">PHYSIOTHERAPY &amp; SPORTS CLINIC</div>
      </div>
    </div>
    <div class="contact">
      <div class="phone">
        <svg width="14" height="14" viewBox="0 0 24 24"><path d="M6.6 10.8a15 15 0 0 0 6.6 6.6l2.2-2.2a1 1 0 0 1 1-.25 11.4 11.4 0 0 0 3.6.57 1 1 0 0 1 1 1V20a1 1 0 0 1-1 1A17 17 0 0 1 3 4a1 1 0 0 1 1-1h3.5a1 1 0 0 1 1 1c0 1.25.2 2.45.57 3.57a1 1 0 0 1-.25 1z" fill="#2f9f5a"/></svg>
        02 9140 2286, &nbsp;02 9173 5520
      </div>
      <div class="addr">Shop 3, Harbour Walk, 12 Ferris Lane, Northbrook 2070</div>
    </div>
  </div>
</header>

<nav class="nav">
  <ul class="wrap">
    <li class="active">Home</li>
    <li>About us</li>
    <li>Common conditions</li>
    <li>Treatments</li>
    <li>Specialised services</li>
    <li>OH&amp;S / Workplace assessment</li>
    <li>Contact us</li>
  </ul>
</nav>

<section class="hero">
  <div class="hero-photo" role="img" aria-label="Physiotherapist guiding a client through a stretch on a reformer machine"></div>
  <div class="hero-card">
    <h1>Back pain exercise<br>program</h1>
    <p>Get Well - Move Well<br>Enjoy the Freedom Again</p>
    <div class="dots"><span class="on"></span><span></span><span></span><span></span><span></span></div>
  </div>
</section>

<section class="intro">
  <div class="wrap">
    <div class="welcome">
      <h2 class="section-title">Welcome to Tidewell Rehab</h2>
      <div class="welcome-body">
        <div class="welcome-photo" role="img" aria-label="Therapist treating a patient's neck with a massage device"></div>
        <div>
          <p class="welcome-lead">Mes cuml dia sed inenias ingert lot aliqtes dolore ipsum sitet ame.</p>
          <p class="welcome-text">Nemo enim ipsam voluptatem voluptas sit. Aspernatur aut odit aut fugit sed quia conse quuntur magni dolor eseos qui rationevolupta tem nesciunt lacusueni ascet dolingerto otis aliqit sit amet eism com odictor ligulate cotameti dapibu emo enim ipsam voluptatem. Nemo enim ipsam voluptatem voluptas sit. Aspernatur aut odit aut fugit sed quia conse quuntur magni dolor eseos qui rationevolupta tem nesciunt lacusueni ascet dolingerto otis aliqit sit amet eism com odictor ligulate cotameti dapibu emo enim ipsam voluptatem.</p>
        </div>
      </div>
    </div>
    <aside class="news">
      <h2 class="section-title">Latest News</h2>
      <div class="news-item">
        <div class="news-date"><b>15</b><small>Mar</small></div>
        <div>
          <div class="news-title">Donec facilisi ulet</div>
          <div class="news-kicker">Lorem ipsum dolore</div>
          <p class="news-text">Lorem ipsum dolor sit amet, consectetur adipiscing elit. Sed blandit massa vel...</p>
        </div>
      </div>
      <div class="news-item">
        <div class="news-date"><b>11</b><small>Mar</small></div>
        <div>
          <div class="news-title">Donec facilisi ulet</div>
          <div class="news-kicker">Lorem ipsum dolore</div>
          <p class="news-text">Lorem ipsum dolor sit amet, consectetur adipiscing elit. Sed blandit massa vel...</p>
        </div>
      </div>
    </aside>
  </div>
</section>

<section class="wrap services">
  <div class="tile-photo" role="img" aria-label="Therapist working on a client's foot" style="background:linear-gradient(135deg,#cfe6a4,#e8d3c2 55%,#b3c98a)"></div>
  <div class="tile light point-left z1"><div class="tile-icon"></div><h3>Physiotherapy</h3><p>Maseleme leifendeuctor wisnes nera iliquam eratutpas.</p><span class="more">Read more</span></div>
  <div class="tile-photo" role="img" aria-label="Client relaxing during a back massage" style="background:linear-gradient(135deg,#d8b89a,#b88a6a 55%,#7a5a44)"></div>
  <div class="tile lime point-left z1"><div class="tile-icon"></div><h3>Massage</h3><p>Maseleme leifendeuctor wisnes nera iliquam eratutpas.</p><span class="more">Read more</span></div>

  <div class="tile lime point-right z1"><div class="tile-icon"></div><h3>Sports Injuries Rehabilitation</h3><p>Maseleme leifendeuctor wisnes nera iliquam eratutpas.</p><span class="more">Read more</span></div>
  <div class="tile-photo" role="img" aria-label="Hands holding a painful knee" style="background:linear-gradient(135deg,#8a8a8a,#3a3a3a 55%,#b0403a)"></div>
  <div class="tile deep point-right z1"><div class="tile-icon"></div><h3>Women's Health</h3><p>Maseleme leifendeuctor wisnes nera iliquam eratutpas.</p><span class="more">Read more</span></div>
  <div class="tile-photo" role="img" aria-label="Clinician consulting with a female patient" style="background:linear-gradient(135deg,#eef1f4,#b9c6d2 55%,#7d8fa3)"></div>

  <div class="tile-photo" role="img" aria-label="Woman exercising on a Pilates reformer" style="background:linear-gradient(135deg,#f2f2f2,#c8c8c8 60%,#4a4a4a)"></div>
  <div class="tile light point-left z1"><div class="tile-icon"></div><h3>Pilates Classes</h3><p>Maseleme leifendeuctor wisnes nera iliquam eratutpas.</p><span class="more">Read more</span></div>
  <div class="tile-photo" role="img" aria-label="Hands pressing on a sore lower back" style="background:linear-gradient(135deg,#c98a6a,#d8563a 50%,#a86a50)"></div>
  <div class="tile lime point-left z1"><div class="tile-icon"></div><h3>Back Pain Exercise Program</h3><p>Maseleme leifendeuctor wisnes nera iliquam eratutpas.</p><span class="more">Read more</span></div>
</section>

<section class="lists">
  <div class="wrap">
    <div>
      <h4>We Treat</h4>
      <ul><li>Back and low back pain</li><li>Neck pain and Headaches</li><li>Spinal/ Posture disorders</li><li>Sport injuries</li><li>Work Injuries/ Motor vehicle accident (whiplash)</li><li>Knee/shoulder pain</li><li>Arthritis</li></ul>
      <span class="details">More Details</span>
    </div>
    <div>
      <h4>We Offer</h4>
      <ul><li>Back and low back pain</li><li>Neck pain and Headaches</li><li>Spinal/ Posture disorders</li><li>Sport injuries</li><li>Work Injuries/ Motor vehicle accident (whiplash)</li><li>Knee/shoulder pain</li><li>Arthritis</li></ul>
      <span class="details">More Details</span>
    </div>
    <div>
      <h4>Specialised Services Include</h4>
      <ul><li>Back and low back pain</li><li>Neck pain and Headaches</li><li>Spinal/ Posture disorders</li><li>Sport injuries</li><li>Work Injuries/ Motor vehicle accident (whiplash)</li><li>Knee/shoulder pain</li><li>Arthritis</li></ul>
      <span class="details">More Details</span>
    </div>
  </div>
</section>

<section class="partners" aria-label="Health fund partners">
  <span class="partner" style="width:58px"></span>
  <span class="partner" style="width:50px"></span>
  <span class="partner" style="width:62px;background:#bdbdbd"></span>
  <span class="partner" style="width:92px;background:#9a9a9a"></span>
  <span class="partner" style="width:92px;background:#8a8a8a"></span>
</section>

<footer class="bottom">
  <div class="wrap">
    <div class="brand">
      <span class="brand-mark"></span>
      <div>
        <div class="brand-name">tidewellrehab</div>
        <div class="brand-sub">PHYSIOTHERAPY &amp; SPORTS CLINIC</div>
      </div>
    </div>
    <div class="info">
      <h5>For Appointments</h5>
      <p>Westbay: 02 9140 2286<br>Northbrook: 02 9173 5520</p>
    </div>
    <div class="info">
      <h5>Opening Hours</h5>
      <p>Monday to Friday: 8am - 7pm<br>Saturday: 8am - 1pm</p>
    </div>
    <div class="social"><span></span><span></span><span></span><span></span></div>
  </div>
</footer>

</body>
</html>
```